Stationery Design Project

See the detainl of the Basic company project I also have live: http://jobs.briefmarlo.com/job.aspx?id=382917

Reason: I am waiting to select a logo design and ideally the stationery will be from the same person

Industry/Entity Type

It Company

```html
<!DOCTYPE html>
<html lang="en">
<head>
<meta charset="utf-8">
<title>Varnel LLP Stationery</title>
<link href="https://fonts.googleapis.com/css2?family=Roboto:wght@500&family=Roboto+Mono&display=swap" rel="stylesheet">
<style>
  :root {
    --backdrop: #6f6f6f;
    --ink-dark: #161616;
    --flap-dark: #1f1f1f;
    --paper: #ffffff;
    --brand-blue: #3d7fd9;
    --fine-text: #3a3a3a;
    --card-text: #cfcfcf;
    --disc-ring: #555555;
    --disc-hole: #8a8a8a;
  }
  * { margin: 0; padding: 0; box-sizing: border-box; }
  html, body { width: 1200px; height: 899px; overflow: hidden; background: var(--backdrop); }
  .canvas { position: relative; width: 1200px; height: 899px; }
  .piece { position: absolute; }
  .brand-name {
    position: absolute;
    font-family: "Roboto", Arial, sans-serif;
    font-weight: 500;
    color: var(--brand-blue);
    white-space: nowrap;
    line-height: 1;
  }
  .envelope-large { left: 90px; top: 202px; width: 326px; height: 497px; }
  .envelope-large .brand-name { left: 25px; top: 448px; font-size: 24px; }
  .letterhead { left: 440px; top: 298px; width: 308px; height: 398px; background: var(--paper); }
  .letterhead .brand-name { left: 19px; top: 23px; font-size: 21px; }
  .letterhead-footer {
    position: absolute; left: 0; right: 0; bottom: 14px;
    text-align: center;
    font-family: "Roboto Mono", monospace;
    font-size: 6.2px; line-height: 9px; color: var(--fine-text);
  }
  .card-front { left: 772px; top: 298px; width: 126px; height: 75px; background: var(--paper); }
  .card-front .brand-name { left: 9px; top: 50px; font-size: 14px; }
  .card-back { left: 772px; top: 394px; width: 126px; height: 73px; background: var(--ink-dark); padding: 7px 9px; }
  .card-back p {
    font-family: "Roboto Mono", monospace;
    font-size: 4.8px; line-height: 6.2px; color: var(--card-text); white-space: nowrap;
  }
  .card-rule { height: 0; border-top: 0.5px solid #5a5a5a; margin: 2px 0 3px; }
  .disc { left: 921px; top: 297px; width: 170px; height: 170px; }
  .disc .brand-name { left: 4px; top: 80px; font-size: 12px; }
  .envelope-small { left: 772px; top: 507px; width: 343px; height: 192px; }
  .envelope-small .brand-name { left: 18px; top: 150px; font-size: 26px; }
  svg.shape { position: absolute; left: 0; top: 0; }
</style>
</head>
<body>
<main class="canvas">

  <section class="piece envelope-large" aria-label="Large envelope">
    <svg class="shape" width="326" height="497" viewBox="0 0 326 497">
      <rect x="0" y="61" width="326" height="436" fill="var(--ink-dark)"/>
      <polygon points="13,0 313,0 326,61 0,61" fill="var(--flap-dark)"/>
    </svg>
    <span class="brand-name">Varnel LLP</span>
  </section>

  <section class="piece letterhead" aria-label="Letterhead">
    <span class="brand-name">Varnel LLP</span>
    <div class="letterhead-footer">
      120 Alder Way, Glenhaven, California 90210<br>
      T. + 1 310 555 0148 &nbsp;E. dana@varnelmail.com &nbsp;www.varnelstudio.info
    </div>
  </section>

  <section class="piece card-front" aria-label="Business card front">
    <span class="brand-name">Varnel LLP</span>
  </section>

  <section class="piece card-back" aria-label="Business card back">
    <p>Dana Wirth</p>
    <p>Brand Design &amp; Direction</p>
    <p>Mobile + 1 310 555 0148</p>
    <p>dana@varnelmail.com</p>
    <div class="card-rule"></div>
    <p>Los Angeles, CA</p>
    <p>www.varnelstudio.info</p>
    <p>www.varnelworks.com</p>
  </section>

  <section class="piece disc" aria-label="Disc label">
    <svg class="shape" width="170" height="170" viewBox="0 0 170 170">
      <circle cx="85" cy="85" r="85" fill="var(--ink-dark)"/>
      <circle cx="85" cy="85" r="23" fill="var(--disc-ring)"/>
      <circle cx="85" cy="85" r="13" fill="var(--disc-hole)"/>
    </svg>
    <span class="brand-name">Varnel LLP</span>
  </section>

  <section class="piece envelope-small" aria-label="Business envelope">
    <svg class="shape" width="343" height="192" viewBox="0 0 343 192">
      <rect x="0" y="46" width="343" height="146" fill="var(--ink-dark)"/>
      <polygon points="13,0 331,0 343,46 0,46" fill="var(--flap-dark)"/>
    </svg>
    <span class="brand-name">Varnel LLP</span>
  </section>

</main>
</body>
</html>
```